Business Cards for Retail/Sourcing Business.

We need a business cards for our company where it looks like:
TK
LV

VERTICAL, where the TK is over the LV. Then Under the TKLV would be name, address and website address. We want the P to be in the style of our original logo, which I uploaded.

Also, can we get a couple of designs with fun colors - especially for the letter head.

Target Market(s)

Old clients. Many of our clients or people we do business with are 40-50 plus. We are not an industry with many young people.

Industry/Entity Type

Business

Contact Information for Business Card

Front side is just says TKLV with name, title, address, and website below.

Font styles to use
Serif
Sans Serif
Decorative
Script

Requirements
Must have
• THE TKLV design with the P in the design of the logo
Nice to have
• Fun colors, new takes on the TKLV and any other additions that would be cool and make it pop

```html
<!DOCTYPE html>
<html lang="en">
<head>
<meta charset="utf-8">
<title>TKLV Business Cards</title>
<link rel="stylesheet" href="https://fonts.googleapis.com/css2?family=Michroma&family=Open+Sans:wght@400;600&display=swap">
<style>
  :root {
    --stage: #bdbdbd;
    --paper: #ffffff;
    --pink: #e8358f;
    --orange: #f47a1f;
    --orange-deep: #e2571c;
    --yellow: #ffe600;
    --sky: #3fb6ea;
    --lime: #9bcf3a;
    --purple: #9a4fa8;
    --ink: #1d1d1d;
  }
  * { box-sizing: border-box; margin: 0; padding: 0; }
  html, body {
    width: 1200px; height: 800px; overflow: hidden;
    background: var(--stage);
  }
  .stage {
    position: relative; width: 1200px; height: 800px;
    display: flex; justify-content: center; align-items: center; gap: 70px;
  }
  .card {
    position: relative; width: 340px; height: 620px;
    background: var(--paper); overflow: hidden;
    box-shadow: 0 4px 14px rgba(0,0,0,0.25);
  }
  .card__burst {
    position: absolute; inset: 0;
    background:
      radial-gradient(ellipse at 50% 48%, #fff 0%, #fff 32%, rgba(255,255,255,0.55) 48%, rgba(255,255,255,0) 70%),
      conic-gradient(from 300deg at 50% 48%,
        var(--pink) 0deg, var(--orange) 50deg, var(--yellow) 100deg,
        #fff7a8 150deg, var(--yellow) 190deg, var(--lime) 215deg,
        var(--yellow) 240deg, var(--sky) 280deg, #bfe7fa 310deg, var(--pink) 360deg);
  }
  .card__burst--back {
    background:
      radial-gradient(ellipse at 50% 42%, #fff 0%, #fff 24%, rgba(255,255,255,0.5) 42%, rgba(255,255,255,0) 66%),
      conic-gradient(from 300deg at 50% 42%,
        var(--pink) 0deg, var(--orange) 45deg, var(--yellow) 95deg,
        #fff7a8 140deg, var(--yellow) 180deg, var(--lime) 210deg,
        var(--yellow) 240deg, var(--sky) 275deg, #bfe7fa 305deg, var(--pink) 360deg);
  }
  .brand {
    position: absolute; left: 0; right: 0;
    font-family: "Michroma", sans-serif;
    text-align: center; line-height: 1.0; letter-spacing: 2px;
  }
  .brand--front { top: 150px; font-size: 82px; color: var(--orange); }
  .brand--back { top: 130px; font-size: 96px; color: var(--purple); }
  .details {
    position: absolute; left: 40px; top: 388px; color: var(--ink);
  }
  .details__name {
    font-family: "Michroma", sans-serif; font-size: 22px;
    color: var(--orange-deep); letter-spacing: 1px;
  }
  .details__title {
    font-family: "Michroma", sans-serif; font-size: 10px;
    letter-spacing: 1.5px; margin-top: 4px; font-variant: small-caps;
  }
  .details__line {
    display: flex; align-items: center; gap: 8px;
    font-family: "Open Sans", sans-serif; font-size: 14px; margin-top: 8px;
  }
  .details__line svg { width: 14px; height: 16px; flex: none; }
</style>
</head>
<body>
<main class="stage">
  <section class="card card--front">
    <div class="card__burst" role="img" aria-label="Colourful swirling sunburst of pink, orange, yellow and blue rays"></div>
    <h1 class="brand brand--front">TK<br>LV</h1>
    <div class="details">
      <p class="details__name">Marlo Vetrane</p>
      <p class="details__title">Home Sourcing cslor.</p>
      <p class="details__line">
        <svg viewBox="0 0 14 16"><path d="M7 0a5.5 5.5 0 0 0-5.5 5.5C1.5 10 7 16 7 16s5.5-6 5.5-10.5A5.5 5.5 0 0 0 7 0z" fill="var(--orange)"/><circle cx="7" cy="5.5" r="2" fill="#fff"/></svg>
        14 Harbor Lane, LV, NV 8910
      </p>
      <p class="details__line">
        <svg viewBox="0 0 16 16"><circle cx="8" cy="8" r="7" fill="none" stroke="var(--orange)" stroke-width="1.6"/><ellipse cx="8" cy="8" rx="3" ry="7" fill="none" stroke="var(--orange)" stroke-width="1.3"/><path d="M1 8h14M2.5 4.5h11M2.5 11.5h11" stroke="var(--orange)" stroke-width="1.1"/></svg>
        yourwebsite
      </p>
    </div>
  </section>

  <section class="card card--back">
    <div class="card__burst card__burst--back" role="img" aria-label="Colourful swirling sunburst of pink, orange, yellow, green and blue rays"></div>
    <p class="brand brand--back">TK<br>LV</p>
  </section>
</main>
</body>
</html>
```